(Wordpress)Website Design - No requirements! Sign Your name at the bottom of the site!

Dear Designer,

I am looking for a designer who is interested in a long-term business realtionship.
I already have 2 more designs to get done IMMEDIATELY after this website..
1.) An email brochure matching the website theme.
2.) A Billboard. BOTH MATCHING THE WEBSITE THEME

For this project, a bonus WILL be given.

Go to vaultnest.com as Site Inspiration

Please take this opportunity to design an existing wordpress website, FUNDSWIFTLANE.com, in whatever form your creativity takes you

I have no requirements other than a CREATIVE and OUT-OF -THE-BOX Design. Something Pretty and Eye Catching; a website that someone logs onto and doesnt want to leave

I have purchased a theme called velorant. You dont need to use it...But Info can be found at

http://skinbazaar.example/item/velorant-premium-wordpress-theme/full_screen_preview/482715

I have attached my logos and a PDF with a short story about what our company does.

Thank You,
-Tobin
PS I HAVE ANOTHER 2 DESIGNS TO DO AFTER THIS PROJECT.
also, IF YOU KNOW OF SOMEONE WHO DOES SEO WORK, I AM LOOKING FOR A FULL-TIME EMPLOYEE

Target Market(s)

Business Owners in a state of finacial NEED

Industry/Entity Type

Business

Requirements
Must have
• COLORFUL, EYE CATCHING

```html
<!DOCTYPE html>
<html lang="en">
<head>
<meta charset="utf-8">
<title>SwiftLane Capital</title>
<link href="https://fonts.googleapis.com/css2?family=Open+Sans:wght@400;600&family=Ubuntu:wght@400;500&family=Tinos&display=swap" rel="stylesheet">
<style>
:root{
  --page:#d9d9d9;
  --dark:#2f2f2f;
  --panel:#f1f1f1;
  --olive:#4b5a22;
  --olive-dark:#343f15;
  --nav-top:#c9e0a2;
  --nav-bottom:#97bd5c;
  --nav-text:#3d5313;
  --text:#222;
  --blue:#2f5f9a;
  --rule:#b5b5b5;
  --foot-text:#cfcfcf;
  --foot-head:#e5e5e5;
}
*{box-sizing:border-box;margin:0;padding:0}
html,body{width:1200px;height:2618px;overflow:hidden}
body{position:relative;background:var(--page);font-family:"Open Sans",Arial,sans-serif;color:var(--text)}
h2,h3{font-weight:400}
.abs{position:absolute}
.header{left:0;top:0;width:1200px;height:138px;background:linear-gradient(#3a3a3a,#242424);border-bottom:3px solid #151515}
.brand{display:flex;align-items:center;gap:12px;font-family:"Ubuntu",sans-serif;font-weight:400;font-size:40px;color:#e8e8e8}
.brand-dot{width:38px;height:38px;border-radius:50%;background:#5d7f2c}
.header .brand{left:96px;top:44px}
.call{left:779px;top:22px;color:#cfcfcf;font-size:24px}
.call b{color:#fff;font-size:31px;font-weight:400;margin-left:6px}
.search{left:858px;top:75px;width:252px;height:30px;border-radius:6px;background:#1c1c1c;border:1px solid #444}
.search svg{position:absolute;right:8px;top:7px}
.nav{left:96px;top:159px;width:1018px;height:63px;background:linear-gradient(var(--nav-top),var(--nav-bottom));border-radius:3px;display:flex;align-items:center}
.nav a{font-family:"Ubuntu",sans-serif;font-size:17px;color:var(--nav-text);text-decoration:none;padding:0 30px;height:63px;line-height:63px;border-right:1px solid #86a750}
.nav .home{padding:0 24px;display:flex;align-items:center}
.hero{left:96px;top:226px;width:1018px;height:522px;background:linear-gradient(#ffffff,#ececec 70%,#d6d6d6)}
.dot{top:673px;width:30px;height:30px;border-radius:50%}
.plans{left:96px;top:758px;width:1018px;height:394px;background:var(--panel)}
.plan-head{position:absolute;top:0;height:78px;background:linear-gradient(var(--olive),var(--olive-dark));color:#d7e2b0;font-family:"Tinos",serif;font-size:34px;text-align:center;line-height:78px}
.plan{position:absolute;top:78px;height:316px;padding:14px 16px;font-size:13px;line-height:21px;color:#333;border-right:1px solid #cfcfcf}
.btn{display:inline-block;border:1px solid #999;border-radius:3px;background:linear-gradient(#fafafa,#dcdcdc);font-size:13px;padding:7px 13px;color:#222}
.plan .btn{margin-top:12px}
.plans-rule{left:16px;top:348px;width:986px;height:1px;background:#aaa}
.intro-title{left:96px;top:1184px;font-family:"Ubuntu",sans-serif;font-size:30px;color:#111}
.photo{top:1252px;width:325px;height:199px;border:2px solid #2c4a82}
.card{top:1475px;width:325px;font-size:15px;line-height:22px}
.card .lead{font-size:15.5px;color:#111}
.card .blue{color:var(--blue);font-size:13px;line-height:21px;margin-top:14px}
.card .body{color:#444;font-size:13px;line-height:21px;margin-top:18px}
.card .btn{margin-top:22px}
.news-title{left:96px;top:1808px;font-family:"Ubuntu",sans-serif;font-size:30px}
.news{left:100px;width:690px;font-size:13px;line-height:21px;color:#333;padding-left:22px}
.news::before{content:"";position:absolute;left:0;top:5px;width:11px;height:11px;border:2px solid #333;border-radius:50%}
.divider{left:844px;top:1173px;width:1px;height:858px;background:var(--rule)}
.apply-title{left:886px;top:1180px;font-family:"Ubuntu",sans-serif;font-size:30px;color:#333}
.field{left:886px;width:228px}
.field label{display:block;font-size:14.5px;color:#222;margin-bottom:6px}
.field .box{height:31px;background:#e4e4e4;border:1px solid #aaa;border-radius:3px}
.field .select{width:156px;height:28px;background:#eee;border:1px solid #999;border-radius:3px;position:relative}
.field .select::after{content:"";position:absolute;right:8px;top:10px;border:6px solid transparent;border-top-color:#333}
.quote{left:886px;top:1752px;background:#555;color:#fff;font-size:14px;padding:7px 12px;border-radius:2px}
.stay{left:876px;top:1816px;font-family:"Ubuntu",sans-serif;font-size:30px;color:#333}
.social{top:1868px;width:44px;height:44px;border-radius:5px}
.footer{left:0;top:2063px;width:1200px;height:488px;background:var(--dark)}
.foot-col{top:2110px;color:var(--foot-text);font-size:13.5px}
.foot-col h3{font-family:"Ubuntu",sans-serif;font-size:22px;color:var(--foot-head);margin-bottom:26px}
.foot-col li{list-style:none;height:30px}
.foot-about{left:800px;top:2112px;width:320px;font-size:13.5px;line-height:21px;color:var(--foot-text)}
.newsletter{left:718px;top:2388px;font-family:"Ubuntu",sans-serif;font-size:21px;color:#e0e0e0}
.news-input{left:718px;top:2428px;width:256px;height:36px;border-radius:4px;background:linear-gradient(#e6e6e6,#bdbdbd)}
.subscribe{left:986px;top:2428px;width:124px;height:36px;border-radius:4px;background:linear-gradient(#a7c46d,#6f8f37);color:#1f2a09;font-size:15px;font-weight:600;text-align:center;line-height:36px}
.footer-brand{right:86px;top:2488px;font-size:32px;color:#bdbdbd}
.footer-brand .brand-dot{width:30px;height:30px;background:#888}
.bottom{left:0;top:2551px;width:1200px;height:67px;background:#c9c9c9;color:#333;font-size:13px;padding:25px 96px}
</style>
</head>
<body>
<header class="abs header">
  <div class="abs brand"><span class="brand-dot"></span>SwiftLane Capital</div>
  <div class="abs call">Call US 24/7! -<b>888-555-0142</b></div>
  <div class="abs search"><svg width="14" height="14" viewBox="0 0 14 14"><circle cx="6" cy="6" r="4" fill="none" stroke="#bbb" stroke-width="2"/><line x1="9" y1="9" x2="13" y2="13" stroke="#bbb" stroke-width="2"/></svg></div>
</header>

<nav class="abs nav">
  <a class="home" href="#"><svg width="34" height="30" viewBox="0 0 34 30"><path d="M17 2 L32 15 H27 V28 H20 V19 H14 V28 H7 V15 H2 Z" fill="#2f6fb8"/></svg></a>
  <a href="#">ABOUT US</a><a href="#">GET STARTED!</a><a href="#">FREE DOWNLOADS</a><a href="#">SWIFTLANE CHARITY</a>
</nav>

<div class="abs hero" role="img" aria-label="Photo of a business team in suits standing in a row"></div>
<div class="abs dot" style="left:908px;background:#9cbd5f"></div>
<div class="abs dot" style="left:955px;background:#9cbd5f"></div>
<div class="abs dot" style="left:1005px;background:#2a3f8a"></div>

<section class="abs plans">
  <div class="plan-head" style="left:0;width:247px">PLAN1</div>
  <div class="plan-head" style="left:247px;width:266px">PLAN2</div>
  <div class="plan-head" style="left:513px;width:254px">PLAN3</div>
  <div class="plan-head" style="left:767px;width:251px">PLAN4</div>
  <div class="plan" style="left:0;width:247px">Lorem Ipsum is simply dummy text of the printing and typesetting industry. Lorem Ipsum has been the industry's standard dummy text ever since the 1500s, when an unknown printer took a galley of type and scrambled.<br><span class="btn">MORE</span></div>
  <div class="plan" style="left:247px;width:266px">Lorem Ipsum is simply dummy text of the printing and typesetting industry. Lorem Ipsum has been the industry's standard dummy text ever since the 1500s, when an unknown printer took a galley of type and scrambled.<br><span class="btn">MORE</span></div>
  <div class="plan" style="left:513px;width:254px">Lorem Ipsum is simply dummy text of the printing and typesetting industry. Lorem Ipsum has been the industry's standard dummy text ever since the 1500s, when an unknown printer took a galley of type and scrambled.<br><span class="btn">MORE</span></div>
  <div class="plan" style="left:767px;width:251px;border-right:0">Lorem Ipsum is simply dummy text of the printing and typesetting industry. Lorem Ipsum has been the industry's standard dummy text ever since the 1500s, when an unknown printer took a galley of type and scrambled.<br><span class="btn">MORE</span></div>
  <div class="abs plans-rule"></div>
</section>

<h2 class="abs intro-title">Lorem Ipsum is simply and typesetting industry.</h2>
<div class="abs photo" style="left:96px;background:linear-gradient(#e8e8e8,#bfc3c8)" role="img" aria-label="Photo of business people meeting in a lounge"></div>
<div class="abs photo" style="left:448px;background:linear-gradient(#f4f4f4,#c9ccd2)" role="img" aria-label="Photo of a consultant at a computer and a businessman holding a globe"></div>
<div class="abs card" style="left:96px">
  <p class="lead">We have a great team of professionals working around the clock making sure to find the best terms</p>
  <p class="blue">Est omnis dolor shepement adroment aurerumons oaes necessratenemt saepe eveniet redums.</p>
  <p class="body">Etoluptates estabulesu usandaeltaque earurum hictenetura sapiravi. Reiciendis vptatibus ass mailoresallasumes. Asperiores asti repellat aureum ode necessbus saepe....</p>
  <span class="btn">MORE</span>
</div>
<div class="abs card" style="left:456px">
  <p class="lead">We even have a network of business coaches and consultants which offered true, sound business advice!</p>
  <p class="blue">Est omnis dolor shepement adroment aurerumons oaes necessratenemt saepe eveniet redums.</p>
  <p class="body">Etoluptates estabulesu usandaeltaque earurum hictenetura sapiravi. Reiciendis vptatibus ass mailoresallasumes. Asperiores asti repellat aureum ode necessbus saepe....</p>
  <span class="btn">MORE</span>
</div>

<h2 class="abs news-title">Recent News</h2>
<p class="abs news" style="top:1856px">Lorem Ipsum is simply dummy text of the printing and typesetting industry. Lorem Ipsum has been the industry's standard dummy text ever since the 1500s.</p>
<p class="abs news" style="top:1924px">Lorem Ipsum is simply dummy text of the printing and typesetting industry. Lorem Ipsum has been the industrs.</p>
<p class="abs news" style="top:1988px">Lorem Ipsum is simply dummy text of the printing and typesetting industry. Lorem Ipsum has been the industry's standard dummy text ever since the 1500s.</p>

<div class="abs divider"></div>
<aside>
  <h2 class="abs apply-title">APPLY</h2>
  <div class="abs field" style="top:1250px"><label>Company Name</label><div class="box"></div></div>
  <div class="abs field" style="top:1314px"><label>First Name</label><div class="box"></div></div>
  <div class="abs field" style="top:1378px"><label>Last Name</label><div class="box"></div></div>
  <div class="abs field" style="top:1442px"><label>Phone</label><div class="box"></div></div>
  <div class="abs field" style="top:1506px"><label>Email</label><div class="box"></div></div>
  <div class="abs field" style="top:1570px"><label>Business Age</label><div class="select"></div></div>
  <div class="abs field" style="top:1634px;width:200px"><label>Monthly Payvex/ CardMint Sales</label><div class="select" style="margin-top:10px;width:190px"></div></div>
  <span class="abs quote">Get My Quote!</span>
  <h2 class="abs stay">Stay Connected</h2>
  <div class="abs social" style="left:882px;background:#1f6fa8"></div>
  <div class="abs social" style="left:934px;background:#3b5998"></div>
  <div class="abs social" style="left:986px;background:#3aa9d9"></div>
  <div class="abs social" style="left:1038px;background:#c8402f"></div>
</aside>

<footer class="abs footer"></footer>
<div class="abs foot-col" style="left:109px"><h3>Personal Backup</h3><ul><li>VaultNest PRO</li><li>Overview</li><li>Features</li><li>Desktop Features</li><li>PRO Online Features</li><li>Mobile Features</li><li>Product Comparison</li><li>How We Stack Up</li><li>VaultNest PRO FAQ</li><li>Sign Up / Free Trial</li><li>Buy</li><li>Support</li></ul></div>
<div class="abs foot-col" style="left:362px"><h3>Business Backup</h3><ul><li>VaultNest PRO</li><li>Overview</li><li>Features</li><li>Desktop Features</li><li>PRO Online Features</li><li>Mobile Features</li><li>Product Comparison</li><li>How We Stack Up</li><li>VaultNest PRO FAQ</li><li>Sign Up / Free Trial</li><li>Buy</li><li>Support</li></ul></div>
<div class="abs foot-col" style="left:620px"><h3>Others</h3><ul><li>Corefold Home</li><li>About Us</li><li>Careers</li><li>Contact Us</li><li>Buzz</li><li>Blog</li></ul></div>
<p class="abs foot-about">Lorem Ipsum is simply dummy text of the printing and typesetting industry. Lorem Ipsum has been the industry's standard dummy text ever since the 1500s, when an unknown printer took a galley of type and scrambled it to make a type specimen book. It has survived not only five centuries, but also the leap into electronic typesetting, remaining essentially unchanged.when an unknown printer took a galley of type and scrambled it to make a type remaining essentially unchanged.</p>
<h3 class="abs newsletter">SignUp for Newsletter</h3>
<div class="abs news-input"></div>
<div class="abs subscribe">SUBSCRIBE</div>
<div class="abs brand footer-brand"><span class="brand-dot"></span>SwiftLane Capital</div>
<div class="abs bottom">© 2012 &nbsp;|&nbsp; Privacy Policy &nbsp;|&nbsp; All Rights Reserved</div>
</body>
</html>
```